Law Firm Business Card

This is a business card for a law firm that serves US military and veterans.

The card must have ONLY the following (we want an uncluttered look):

- Company logo (PNG, GIF, JPEG copies uploaded)
- A tagline reading: "a law firm for service members and veterans"
- My name and title: "Martin Okello" and "Attorney"
- My email: "martin.okello@harborlinecounsel.com"
- My number: "855-FILE-NOW (345-3669)"

We are looking for a clean, simple layout with only the above information, likely printed on a bright white cotton stock. The font of our logo is DIN 1451, and the font used on our website is Helvetica Neue. The color of our logo is #336699, and we probably want the tagline in that color also, and my contact information in a dark grey. Please review our website at www.harborlinecounsel.com to ensure your card design complements our website style.

Thanks and we look forward to seeing your submissions.

A few notes:

- Two-sided submissions are ok
- Please don't add graphics (scales of justice, judges hammer, etc)

```html
<!DOCTYPE html>
<html lang="en">
<head>
<meta charset="utf-8">
<title>Harborline Counsel – Business Card Options</title>
<link rel="stylesheet" href="https://fonts.googleapis.com/css2?family=Open+Sans:wght@400;600&family=Italianno&display=swap">
<style>
  :root {
    --board: #e2c2a4;
    --label-ink: #3a3330;
    --rule: #8f7f72;
    --brand-blue: #336699;
    --band-edge: #244f7a;
    --card-white: #ffffff;
    --name-light: #c9d0da;
    --title-light: #b9c3cf;
    --contact-ink: #2b5a8a;
  }
  * { margin: 0; padding: 0; box-sizing: border-box; }
  html, body { width: 1200px; height: 1200px; overflow: hidden; }
  body {
    background: var(--board);
    font-family: "Open Sans", "Helvetica Neue", Arial, sans-serif;
    position: relative;
  }
  .option-label {
    position: absolute;
    font-family: "Italianno", cursive;
    font-size: 70px;
    line-height: 1;
    color: var(--label-ink);
    padding-bottom: 6px;
    border-bottom: 1.5px solid var(--rule);
    text-align: center;
  }
  .option-label--two { left: 143px; top: 143px; width: 335px; }
  .option-label--one { left: 735px; top: 345px; width: 305px; }

  .card {
    position: absolute;
    width: 517px;
    background: var(--card-white);
    overflow: hidden;
    display: flex;
    flex-direction: column;
  }
  .band { background: var(--brand-blue); }
  .band--edged { border-bottom: 2px solid var(--band-edge); }

  .wordmark {
    color: var(--brand-blue);
    font-weight: 600;
    text-align: center;
    line-height: 1;
  }
  .wordmark__main { display: block; letter-spacing: 0.5px; }
  .wordmark__sub { display: block; letter-spacing: 5px; }
  .tagline {
    color: var(--brand-blue);
    text-align: center;
    font-weight: 400;
  }

  /* Two-sided: front */
  .card--front { left: 50px; top: 255px; height: 297px; }
  .card--front .band { height: 97px; }
  .card--front .brand-strip {
    height: 103px;
    display: flex; flex-direction: column; align-items: center; justify-content: center;
  }
  .card--front .wordmark__main { font-size: 35px; }
  .card--front .wordmark__sub { font-size: 19px; margin-top: 4px; }
  .card--front .tagline { font-size: 11px; margin-top: 10px; }

  /* Two-sided: back */
  .card--back { left: 50px; top: 650px; height: 292px; }
  .card--back .spacer { height: 87px; }
  .card--back .band {
    height: 118px;
    display: flex; flex-direction: column; align-items: center; justify-content: center;
    color: var(--card-white);
  }
  .card--back .person-name { font-size: 30px; font-weight: 400; line-height: 1.1; }
  .card--back .person-title { font-size: 19px; letter-spacing: 5px; margin-top: 8px; font-weight: 600; }
  .card--back .contact {
    flex: 1;
    display: flex; align-items: center; justify-content: center;
    font-size: 11.5px; color: var(--contact-ink);
  }

  /* One-sided */
  .card--single { left: 630px; top: 453px; height: 292px; }
  .card--single .brand-strip {
    height: 122px;
    display: flex; flex-direction: column; align-items: center; justify-content: center;
    padding-top: 6px;
  }
  .card--single .wordmark__main { font-size: 28px; }
  .card--single .wordmark__sub { font-size: 16px; margin-top: 3px; }
  .card--single .tagline { font-size: 10.5px; margin-top: 8px; }
  .card--single .band {
    height: 87px;
    display: flex; flex-direction: column; align-items: center; justify-content: center;
  }
  .card--single .person-name { font-size: 22px; color: var(--name-light); font-weight: 600; line-height: 1.1; }
  .card--single .person-title { font-size: 15px; color: var(--title-light); margin-top: 1px; }
  .card--single .contact {
    flex: 1;
    display: flex; flex-direction: column; align-items: center; justify-content: center;
    font-size: 11px; line-height: 1.6; color: var(--contact-ink);
  }
</style>
</head>
<body>
  <div class="option-label option-label--two">Two Sided</div>

  <section class="card card--front" aria-label="Card front">
    <div class="band"></div>
    <div class="brand-strip">
      <div class="wordmark">
        <span class="wordmark__main">HARBORLINE</span>
        <span class="wordmark__sub">COUNSEL</span>
      </div>
      <p class="tagline">a law firm for service members and veterans</p>
    </div>
    <div class="band"></div>
  </section>

  <section class="card card--back" aria-label="Card back">
    <div class="spacer"></div>
    <div class="band band--edged">
      <p class="person-name">Martin Okello</p>
      <p class="person-title">Attorney</p>
    </div>
    <p class="contact">martin.okello@harborlinecounsel.com || 855-FILE-NOW (345-3669)</p>
  </section>

  <div class="option-label option-label--one">One Sided</div>

  <section class="card card--single" aria-label="Single-sided card">
    <div class="brand-strip">
      <div class="wordmark">
        <span class="wordmark__main">HARBORLINE</span>
        <span class="wordmark__sub">COUNSEL</span>
      </div>
      <p class="tagline">a law firm for service members and veterans</p>
    </div>
    <div class="band band--edged">
      <p class="person-name">Martin Okello</p>
      <p class="person-title">Attorney</p>
    </div>
    <div class="contact">
      <span>martin.okello@harborlinecounsel.com</span>
      <span>855-FILE-NOW (345-3669)</span>
    </div>
  </section>
</body>
</html>
```